Business card

Hi Marta,
can you please design business cards for me?
Based on your Brimvale design please go crazy (still retain a professional business-solid profile). I would like to use really stylish paper (or different paper types and special prints like partly embossed or partly glossy and contrast the glossiness with matt for instance).
Please keep in mind that I might come back to you in several months if the business requires other print material like stationary, folders, envelopes etc. It all needs to be in line and make a huge impression without going over board and still remain very solid and serious.
I know that's a lot to ask and I apologise but I am really impressed with your work so far and have no doubt that you can spin the wheels again in a great way.
Thanks bunches, Lukas
In order to punch in the right text from the outset, here is some key data:
Brimvale
Rise beyond
Lukas Brander
Chief Executive Growth Partner
+41 79 583 1067
lukas.brander@brimvale.com
brimvale.com
Business
Brimvale
Rise beyond
Lukas Brander
+41 79 583 1067
brimvale.com

```html
<!DOCTYPE html>
<html lang="en">
<head>
<meta charset="utf-8">
<title>Brimvale — Business Card Specification</title>
<link rel="stylesheet" href="https://fonts.googleapis.com/css2?family=Fira+Sans:wght@300;400;500;600&display=swap">
<style>
  :root {
    --stage-light: #ffffff;
    --stage-edge: #d9d9d9;
    --matt-black: #2a2423;
    --gloss-black: #100c0c;
    --callout-red: #d42027;
    --ink-white: #ffffff;
    --ink-grey: #8c8684;
    --spec-ink: #1c1c1c;
  }
  html, body {
    margin: 0;
    padding: 0;
    width: 1079px;
    height: 1200px;
    overflow: hidden;
  }
  body {
    background: radial-gradient(ellipse at 50% 45%, var(--stage-light) 30%, var(--stage-edge) 100%);
  }
  .spec-sheet {
    display: block;
    width: 1079px;
    height: 1200px;
  }
  .card-matt { fill: var(--matt-black); }
  .card-gloss { fill: var(--gloss-black); }
  .callout-label {
    font-family: "Fira Sans", sans-serif;
    font-weight: 500;
    font-size: 15px;
    letter-spacing: 0.6px;
    fill: var(--callout-red);
  }
  .callout-ring {
    fill: none;
    stroke: var(--callout-red);
    stroke-width: 2.6;
    stroke-dasharray: 7 4;
  }
  .callout-leader {
    stroke: var(--callout-red);
    stroke-width: 2;
    stroke-dasharray: 1 3;
    stroke-linecap: round;
  }
  .brand-name {
    font-family: "Fira Sans", sans-serif;
    font-weight: 300;
    font-size: 32px;
    fill: var(--ink-white);
  }
  .brand-tagline {
    font-family: "Fira Sans", sans-serif;
    font-size: 9px;
    fill: var(--ink-grey);
  }
  .holder-name {
    font-family: "Fira Sans", sans-serif;
    font-weight: 600;
    font-size: 15px;
    fill: var(--ink-white);
  }
  .holder-title,
  .holder-contact {
    font-family: "Fira Sans", sans-serif;
    font-weight: 300;
    font-size: 13px;
    fill: var(--ink-grey);
  }
  .holder-web {
    font-family: "Fira Sans", sans-serif;
    font-weight: 600;
    font-size: 13px;
    fill: var(--ink-white);
  }
  .size-heading,
  .size-values {
    font-family: "Fira Sans", sans-serif;
    font-weight: 500;
    font-size: 15px;
    fill: var(--spec-ink);
  }
  .size-values .figure { font-weight: 400; font-size: 18px; }
</style>
</head>
<body>
<svg class="spec-sheet" viewBox="0 0 809 900" xmlns="http://www.w3.org/2000/svg" role="img" aria-label="Brimvale business card specification, front and back">

  <g class="card-front">
    <polygon class="card-matt" points="268,118 660,118 660,268 541,430 148,430 148,282"/>
    <polygon class="card-gloss" points="516,118 660,118 660,268 541,430 290,430"/>
    <text class="brand-name" x="391" y="275" text-anchor="middle" textLength="282" lengthAdjust="spacing">BRIMVALE</text>
    <text class="brand-tagline" x="391" y="295" text-anchor="middle" textLength="135" lengthAdjust="spacing">RISE BEYOND</text>
  </g>

  <g class="card-back">
    <polygon class="card-matt" points="148,466 541,466 660,628 660,778 268,778 148,618"/>
    <polygon class="card-gloss" points="518,466 541,466 660,628 660,666"/>
    <polygon class="card-gloss" points="148,566 148,618 268,778 298,778"/>
    <text class="holder-name" x="404" y="569" text-anchor="middle" textLength="148" lengthAdjust="spacing">LUKAS BRANDER</text>
    <text class="holder-title" x="404" y="594" text-anchor="middle">Chief Executive Growth Partner</text>
    <text class="holder-contact" x="404" y="666" text-anchor="middle" textLength="325" lengthAdjust="spacing">+41 79 583 1067 • lukas.brander@brimvale.com</text>
    <text class="holder-web" x="404" y="693" text-anchor="middle">brimvale.com</text>
  </g>

  <g class="callouts-front">
    <text class="callout-label" x="275" y="55" textLength="108" lengthAdjust="spacing">MATT BLACK</text>
    <line class="callout-leader" x1="398" y1="52" x2="460" y2="132"/>
    <circle class="callout-ring" cx="466" cy="143" r="12"/>

    <text class="callout-label" x="617" y="55" textLength="118" lengthAdjust="spacing">GLOSS BLACK</text>
    <line class="callout-leader" x1="606" y1="52" x2="544" y2="132"/>
    <circle class="callout-ring" cx="537" cy="143" r="12"/>

    <text class="callout-label" x="42" y="201">“BRIMVALE”</text>
    <text class="callout-label" x="42" y="230" textLength="120" lengthAdjust="spacing">IN DEBOSSED</text>
    <text class="callout-label" x="42" y="258" textLength="53" lengthAdjust="spacing">PRINT</text>
    <line class="callout-leader" x1="115" y1="255" x2="234" y2="255"/>
    <circle class="callout-ring" cx="248" cy="254" r="12"/>

    <circle class="callout-ring" cx="597" cy="354" r="12"/>
    <line class="callout-leader" x1="612" y1="355" x2="735" y2="355"/>
    <text class="callout-label" x="681" y="375" textLength="100" lengthAdjust="spacing">CNC/LASER</text>
    <text class="callout-label" x="681" y="402" textLength="79" lengthAdjust="spacing">CUTTING</text>
    <text class="callout-label" x="681" y="430" textLength="86" lengthAdjust="spacing">TO SHAPE</text>
  </g>

  <g class="callouts-back">
    <text class="callout-label" x="20" y="557" textLength="109" lengthAdjust="spacing">MATT BLACK</text>
    <line class="callout-leader" x1="58" y1="567" x2="176" y2="567"/>
    <circle class="callout-ring" cx="190" cy="566" r="12"/>

    <text class="callout-label" x="20" y="641" textLength="117" lengthAdjust="spacing">GLOSS BLACK</text>
    <line class="callout-leader" x1="58" y1="653" x2="176" y2="653"/>
    <circle class="callout-ring" cx="190" cy="652" r="12"/>

    <text class="callout-label" x="681" y="557" textLength="118" lengthAdjust="spacing">GLOSS BLACK</text>
    <circle class="callout-ring" cx="597" cy="566" r="12"/>
    <line class="callout-leader" x1="612" y1="567" x2="735" y2="567"/>

    <text class="callout-label" x="682" y="641" textLength="109" lengthAdjust="spacing">MATT BLACK</text>
    <circle class="callout-ring" cx="597" cy="650" r="12"/>
    <line class="callout-leader" x1="612" y1="651" x2="735" y2="651"/>
  </g>

  <g class="size-note">
    <text class="size-heading" x="404" y="826" text-anchor="middle" textLength="190" lengthAdjust="spacing">BUSINESS CARD SIZE:</text>
    <text class="size-values" x="404" y="854" text-anchor="middle" textLength="318" lengthAdjust="spacing">WIDTH: <tspan class="figure">90</tspan> MM  |  HEIGHT: <tspan class="figure">55</tspan> MM</text>
  </g>
</svg>
</body>
</html>
```